Harlow Ridge Partners Business Cards

Design Business cards in a format where I can change the information and utilize a third party buisness card printing company

Contact Information for Business Card

Want Logo and Name on Back. Looking for Spot UV style shine on Logo. Probably Black background. Want smaller logo on front with contact details. Like rounded edges or something else interesting.

Requirements
Must have
• Strong masculine look.

```html
<!DOCTYPE html>
<html lang="en">
<head>
<meta charset="utf-8">
<title>Harlow Ridge Partners Business Cards</title>
<link rel="stylesheet" href="https://fonts.googleapis.com/css2?family=Montserrat:wght@400;500;700&display=swap">
<style>
  :root {
    --stage: #2b2b2b;
    --card: #1f1f1f;
    --card-edge: #262626;
    --gloss: #0e0e0e;
    --mark-grey: #6f6f6f;
    --divider: #5a5a5a;
    --text-main: #ffffff;
    --text-soft: #e4e4e4;
    --icon: #8a8a8a;
  }
  * { box-sizing: border-box; margin: 0; padding: 0; }
  html, body { width: 1200px; height: 1030px; overflow: hidden; }
  body {
    background: var(--stage);
    font-family: "Montserrat", sans-serif;
    position: relative;
  }
  .card {
    position: absolute;
    left: 200px;
    width: 800px;
    height: 457px;
    background: var(--card);
    border: 1px solid var(--card-edge);
    border-radius: 6px;
    box-shadow: 0 8px 24px rgba(0,0,0,.45);
  }
  .card--back { top: 40px; }
  .card--front { top: 533px; }

  /* Back: name with spot-UV style on black */
  .back-mark {
    position: absolute;
    inset: 0;
    display: flex;
    align-items: center;
    justify-content: center;
    gap: 18px;
  }
  .back-mark .mark-square {
    width: 34px; height: 34px;
    background: var(--gloss);
  }
  .back-mark .mark-name {
    font-weight: 500;
    font-size: 42px;
    letter-spacing: 3px;
    color: var(--gloss);
    text-transform: uppercase;
  }

  /* Front */
  .front-mark {
    position: absolute;
    left: 40px; top: 150px;
    width: 300px;
    display: flex;
    align-items: center;
    gap: 12px;
  }
  .front-mark .mark-square {
    width: 22px; height: 22px; flex: none;
    background: var(--mark-grey);
  }
  .front-mark .mark-name {
    font-weight: 500;
    font-size: 24px;
    line-height: 1.2;
    letter-spacing: 2px;
    color: var(--mark-grey);
    text-transform: uppercase;
  }
  .divider {
    position: absolute;
    left: 372px; top: 95px;
    width: 1px; height: 200px;
    background: var(--divider);
  }
  .contact {
    position: absolute;
    left: 410px; top: 95px;
  }
  .contact .person {
    font-weight: 700;
    font-size: 32px;
    color: var(--text-main);
    letter-spacing: .5px;
  }
  .contact .role {
    margin-top: 4px;
    font-size: 18px;
    color: var(--text-soft);
  }
  .contact ul { list-style: none; margin-top: 26px; }
  .contact li {
    display: flex; align-items: center; gap: 16px;
    font-size: 18px; color: var(--text-soft);
    margin-bottom: 14px;
  }
  .contact svg { width: 20px; height: 20px; flex: none; }
  .address {
    position: absolute;
    left: 0; right: 0; bottom: 52px;
    text-align: center;
    font-size: 19px;
    color: var(--text-soft);
  }
</style>
</head>
<body>
  <section class="card card--back">
    <div class="back-mark">
      <span class="mark-square"></span>
      <span class="mark-name">Harlow Ridge Partners</span>
    </div>
  </section>

  <section class="card card--front">
    <div class="front-mark">
      <span class="mark-square"></span>
      <span class="mark-name">Harlow Ridge Partners</span>
    </div>
    <div class="divider"></div>
    <div class="contact">
      <div class="person">Dorian BLAKE</div>
      <div class="role">Managing Director</div>
      <ul>
        <li>
          <svg viewBox="0 0 24 24" fill="none" stroke="var(--icon)" stroke-width="1.6"><path d="M5 3h4l2 5-2.5 1.5a11 11 0 0 0 6 6L16 13l5 2v4a2 2 0 0 1-2 2A16 16 0 0 1 3 5a2 2 0 0 1 2-2z"/></svg>
          000.000.0000
        </li>
        <li>
          <svg viewBox="0 0 24 24" fill="none" stroke="var(--icon)" stroke-width="1.6"><rect x="3" y="5" width="18" height="14"/><path d="M3 5l9 8 9-8"/></svg>
          dorian@harlowridgepartners.com
        </li>
        <li>
          <svg viewBox="0 0 24 24" fill="none" stroke="var(--icon)" stroke-width="1.6"><circle cx="12" cy="12" r="9"/><path d="M3 12h18M12 3c3 3 3 15 0 18M12 3c-3 3-3 15 0 18"/></svg>
          www.harlowridgepartners.com
        </li>
      </ul>
    </div>
    <div class="address">410-2280 Cedarline Rd Victoria BC V8R 4K7</div>
  </section>
</body>
</html>
```